Start-up lawncare company needing marketing flyer to promote business model

Hello! We are looking for a marketing flyer design with the requirements below.

We would like the size to fit a flyer that is 6.25" X 9", Front and Back.

We need these to meet the NPDS RCMX requirements, there are details attached for the indicias that need to be included, and where to put them on the back of the flyer.

Here's the items items we would like to have included on the flyer:
- Logo (Attached)

- I attached a snip of how our website looks, as well as how our app looks, and would like to follow that general color scheme

- References to our YardMint App, in both Quorvex and Plinth stores, and our website (www.YardMint.example)

- Reference to the neighborhood barometer and gets the point across that the more of their neighbors that sign up, the cheaper the price of service (Visual attached of what this barometer looks like)

- We are licensed and insured landscaping pros

- Real, instant, upfront pricing for mowing, mulching and most other services

- Sign up with a few easy steps and manage your account from our app or online

- Automated safe & secure transactions upon service completion and satisfaction

- Excellent customer service with our quality guaranteed commitment!

- Sign up now and receive 50% off your first mow!

- Veteran owned

- A portion of our proceeds go to "Rowan Ellery Foundation"

- List's out all of the services we will offer
- Mowing
- Mulching
- Aeration and Over-seeding
- Fertilization
- Shrub/Tree Trimming
- Leaf removal and yard clean up
- Accent lighting installation
- Sprinkler blow-out / Winterization
- Driveway pressure washing and sealing
- Firewood Delivery

Target Market(s)

Homeowners in large neighborhoods that need lawn care services

Industry/Entity Type

Lawn Care

Font styles to use
Sans Serif

Colors

Designer to choose colors to be used in the design.

Requirements
Must have
• Meet NPDS RCMX requirements
• Keep a similar color scheme to our website, feel free to use bold accents to make it more eye-catching as people search through their mail
• Get the general point across that as more of their neighbors sign up with us, the cheaper their service will be

```html
<!DOCTYPE html>
<html lang="en">
<head>
<meta charset="utf-8">
<title>YardMint Mailer – Front and Back</title>
<link rel="stylesheet" href="https://fonts.googleapis.com/css2?family=Oswald:wght@400;500;600&family=Montserrat:wght@600;700;800&family=Roboto+Condensed:wght@400;500&family=Roboto:wght@400;500&display=swap">
<style>
  :root{
    --navy:#21409a;
    --sky:#1f9fe0;
    --green:#2fb24a;
    --green-deep:#1f9a3c;
    --white:#ffffff;
    --ink:#222222;
    --stage:#ececec;
  }
  *{box-sizing:border-box;margin:0;padding:0}
  html,body{width:1200px;height:1200px;overflow:hidden;background:var(--stage)}
  .mailer{position:absolute;width:755px;height:524px;background:var(--white);overflow:hidden}
  .mailer--front{left:64px;top:53px}
  .mailer--back{left:311px;top:622px}
  .mailer svg.art{position:absolute;left:0;top:0}
  .abs{position:absolute}

  /* front */
  .brand{left:18px;top:58px;display:flex;align-items:center;gap:8px}
  .brand__dot{width:16px;height:16px;border-radius:50%;background:var(--green)}
  .brand__name{font:600 30px/1 'Oswald',sans-serif;color:var(--navy)}
  .headline{left:166px;top:14px;font-family:'Oswald',sans-serif;font-weight:600;line-height:1.08}
  .headline__top{color:var(--green);font-size:27px}
  .headline__bottom{color:var(--navy);font-size:25px}
  .signup-pill{left:190px;top:86px;font:600 13.5px/19px 'Montserrat',sans-serif;color:var(--white)}
  .section-title{font:800 16px/1 'Montserrat',sans-serif}
  .why-title{left:15px;top:155px;color:var(--white)}
  .services-title{left:15px;top:304px;color:var(--green-deep);font-weight:700}
  .benefits{left:14px;top:183px;list-style:none;font:400 10.6px/17.4px 'Roboto Condensed',sans-serif;color:var(--white)}
  .benefits li{display:flex;align-items:center;gap:6px}
  .tick{width:9px;height:9px;border:1.3px solid var(--white);position:relative;flex:none}
  .tick::after{content:"";position:absolute;left:2px;top:-1px;width:3px;height:6px;border:solid var(--white);border-width:0 1.5px 1.5px 0;transform:rotate(40deg)}
  .service-list{list-style:none;top:335px;font:500 12px/22px 'Roboto Condensed',sans-serif;color:var(--white)}
  .service-list--a{left:16px}
  .service-list--b{left:188px}
  .service-list li{display:flex;align-items:center;gap:9px}
  .service-list li::before{content:"";width:13px;height:13px;border-radius:50%;background:var(--green);flex:none}
  .contact{font:500 16px/22px 'Oswald',sans-serif;color:var(--white);white-space:nowrap}
  .contact b{font-weight:500}
  .contact span{font-family:'Roboto',sans-serif;font-size:14px;letter-spacing:.5px}
  .front-contact{left:15px;top:467px}
  .offer-lead{left:285px;top:468px;width:106px;text-align:center;font:600 14.5px/19px 'Montserrat',sans-serif;color:var(--white)}
  .offer-big{left:404px;top:460px;font:800 45px/1.2 'Montserrat',sans-serif;color:var(--white)}
  .offer-tail{left:636px;top:468px;width:119px;text-align:center;font:700 16.5px/22px 'Montserrat',sans-serif;color:var(--white)}

  /* back */
  .savings{left:17px;top:12px;font-family:'Oswald',sans-serif;font-weight:500;color:var(--white);line-height:1.05}
  .savings__lead{font-size:24px}
  .savings__big{font-size:40px;font-weight:600}
  .savings__line{font-size:16px}
  .savings__end{font-size:21px}
  .app-callout{left:17px;top:146px;font-family:'Montserrat',sans-serif;color:var(--white);line-height:1.1}
  .app-callout__a{font-weight:700;font-size:12px}
  .app-callout__b{font-weight:700;font-size:9.3px}
  .app-callout__c{font-weight:800;font-size:18.5px;color:var(--sky)}
  .ribbon-text{left:289px;width:129px;text-align:center;color:var(--white);font-family:'Montserrat',sans-serif}
  .ribbon-text--lead{top:120px;font-weight:700;font-size:15px;line-height:20px}
  .ribbon-text--big{top:175px;font-weight:800;font-size:38px;line-height:36px}
  .first-mow{left:274px;top:296px;width:160px;text-align:center;font:800 24px/29px 'Montserrat',sans-serif;color:var(--navy)}
  .meter-label{font:700 11px/1 'Montserrat',sans-serif;color:var(--white);transform:rotate(90deg);transform-origin:left top}
  .back-contact{left:222px;top:398px;font-size:13px;line-height:17px;color:var(--navy)}
  .back-contact span{font-size:11.5px;letter-spacing:.3px;color:var(--ink)}
  .indicia{left:666px;top:318px;width:63px;height:63px;border:1px solid #555;font:400 8px/10px 'Roboto',sans-serif;color:var(--ink);text-align:center;padding-top:4px}
  .indicia b{font-weight:500}
  .address{left:497px;top:414px;width:209px;height:84px;border:1px solid #555;font:400 11px/14px 'Roboto',sans-serif;color:var(--ink);padding:10px 14px}
  .address__route{text-align:right;font-size:9.5px;margin-bottom:16px}
</style>
</head>
<body>

<!-- FRONT -->
<section class="mailer mailer--front">
  <svg class="art" width="755" height="524" viewBox="0 0 755 524">
    <defs>
      <linearGradient id="greenBand" x1="0" y1="0" x2="1" y2="0">
        <stop offset="0" stop-color="#2fb24a"/><stop offset="1" stop-color="#25a894"/>
      </linearGradient>
      <linearGradient id="houseScene" x1="0" y1="0" x2="0" y2="1">
        <stop offset="0" stop-color="#8cc8f0"/><stop offset=".55" stop-color="#8a9aa3"/><stop offset="1" stop-color="#4a9a3a"/>
      </linearGradient>
    </defs>
    <rect x="0" y="147" width="755" height="150" fill="url(#greenBand)"/>
    <polygon points="0,147 160,147 136,178 0,178" fill="#21409a"/>
    <rect x="0" y="295" width="755" height="161" fill="#21409a"/>
    <polygon points="0,297 278,297 252,323 0,323" fill="#ffffff"/>
    <rect x="154" y="81" width="300" height="62" rx="31" fill="#1f9fe0"/>
    <g fill="none" stroke="#fff" stroke-width="1.6">
      <circle cx="172" cy="112" r="5"/><path d="M163 106a11 11 0 0 1 18 0"/><path d="M159 102a16 16 0 0 1 26 0"/>
    </g>
    <polygon points="577,20 755,122.5 755,327.5 577,430 399,327.5 399,122.5" fill="#21409a" stroke="#21409a" stroke-width="14" stroke-linejoin="round"/>
    <polygon points="577,33 743,129 743,321 577,417 411,321 411,129" fill="#ffffff" stroke="#ffffff" stroke-width="10" stroke-linejoin="round"/>
    <polygon role="img" aria-label="Photo of a two-storey house with a green lawn and trimmed shrubs" points="577,47 731,136 731,314 577,403 423,314 423,136" fill="url(#houseScene)" stroke="#8cc8f0" stroke-width="6" stroke-linejoin="round"/>
    <polygon points="0,456 268,456 286,490 268,524 0,524" fill="#1f9fe0"/>
    <polygon points="272,456 755,456 755,524 272,524 290,490" fill="#2fb24a"/>
    <polygon points="268,456 274,456 292,490 274,524 268,524 286,490" fill="#ffffff"/>
    <line x1="634" y1="460" x2="634" y2="520" stroke="#fff" stroke-width="1.5" stroke-dasharray="2 3"/>
  </svg>

  <div class="abs brand"><span class="brand__dot"></span><span class="brand__name">YardMint</span></div>

  <div class="abs headline">
    <div class="headline__top">LANDSCAPING SERVICE</div>
    <div class="headline__bottom">RIGHT AT YOUR FINGERTIPS</div>
  </div>

  <div class="abs signup-pill">Sign Up With a Few Easy Steps<br>And Manage Your Account<br>From Our App or Online</div>

  <h2 class="abs section-title why-title">WHY US</h2>
  <ul class="abs benefits">
    <li><span class="tick"></span>We are licensed and insured landscaping pros</li>
    <li><span class="tick"></span>Real, instant, upfront pricing for mowing, mulching and most other services</li>
    <li><span class="tick"></span>Automated safe &amp; secure transactions upon service completion and satisfaction</li>
    <li><span class="tick"></span>Excellent customer service with our quality guaranteed commitment!</li>
    <li><span class="tick"></span>Veteran owned</li>
    <li><span class="tick"></span>A portion of our proceeds go to "Rowan Ellery Foundation"</li>
  </ul>

  <h2 class="abs section-title services-title">SERVICES WE PROVIDE</h2>
  <ul class="abs service-list service-list--a">
    <li>Mowing</li><li>Mulching</li><li>Aeration and Over-seeding</li><li>Fertilization</li><li>Shrub/Tree Trimming</li>
  </ul>
  <ul class="abs service-list service-list--b">
    <li>Leaf removal and yard clean up</li><li>Accent lighting installation</li><li>Sprinkler blow-out / Winterization</li><li>Driveway pressure washing and sealing</li><li>Firewood Delivery</li>
  </ul>

  <div class="abs contact front-contact">
    <div><b>CALL US</b> ☏ <span>555-0142-386</span></div>
    <div><b>VISIT US</b> ⊕ <span>www.YardMint.example</span></div>
  </div>
  <div class="abs offer-lead">Sign up now<br>and receive</div>
  <div class="abs offer-big">50% OFF</div>
  <div class="abs offer-tail">Your First<br>Mow!</div>
</section>

<!-- BACK -->
<section class="mailer mailer--back">
  <svg class="art" width="755" height="524" viewBox="0 0 755 524">
    <defs>
      <linearGradient id="greenTop" x1="0" y1="0" x2="1" y2="0">
        <stop offset="0" stop-color="#2fb24a"/><stop offset="1" stop-color="#27a86a"/>
      </linearGradient>
      <linearGradient id="ribbon" x1="0" y1="0" x2="0" y2="1">
        <stop offset="0" stop-color="#21409a"/><stop offset="1" stop-color="#1f9fe0"/>
      </linearGradient>
      <linearGradient id="meter" x1="0" y1="0" x2="0" y2="1">
        <stop offset="0" stop-color="#21409a"/><stop offset=".5" stop-color="#1f9fe0"/><stop offset="1" stop-color="#2fb24a"/>
      </linearGradient>
      <linearGradient id="phoneShot" x1="0" y1="0" x2="1" y2="1">
        <stop offset="0" stop-color="#2f9a5a"/><stop offset=".6" stop-color="#e9e9e9"/><stop offset="1" stop-color="#d7a88c"/>
      </linearGradient>
    </defs>
    <polygon points="0,0 282,0 452,98 452,430 336,524 0,524" fill="#21409a" stroke="#21409a" stroke-width="10" stroke-linejoin="round"/>
    <polygon points="0,0 262,0 438,102 438,426 400,454 0,454" fill="#ffffff"/>
    <polygon points="0,0 262,0 438,102 438,137 0,137" fill="url(#greenTop)"/>
    <path d="M0 142 H237 a14 14 0 0 1 14 14 V184 a14 14 0 0 1 -14 14 H0 Z" fill="#21409a"/>
    <path d="M289 128 a14 14 0 0 1 14 -14 H418 V286 L353 256 L289 286 Z" fill="url(#ribbon)"/>
    <path d="M295 168 H412 V276 L353 249 L295 276 Z" fill="none" stroke="#fff" stroke-width="1.5" stroke-dasharray="2 3"/>
    <rect role="img" aria-label="Photo of a hand holding a phone showing the app's instant quote screen" x="17" y="210" width="216" height="314" rx="14" fill="url(#phoneShot)"/>
    <rect x="219" y="206" width="22" height="188" rx="11" fill="url(#meter)"/>
    <polygon points="245,213 253,213 253,208 262,218 253,228 253,223 245,223" fill="#21409a"/>
    <polygon points="245,280 255,280 255,274 266,286 255,298 255,292 245,292" fill="#1f9fe0"/>
    <polygon points="245,344 258,344 258,336 272,352 258,368 258,360 245,360" fill="#2fb24a"/>
  </svg>

  <div class="abs savings">
    <div class="savings__lead">YOU COULD SAVE UP TO</div>
    <div class="savings__big">10% OFF OUR</div>
    <div class="savings__line">ALREADY LOW PRICES, AS MORE OF</div>
    <div class="savings__end">YOUR NEIGHBORS SIGN UP!</div>
  </div>

  <div class="abs app-callout">
    <div class="app-callout__a">CHECK OUT OUR APP TODAY</div>
    <div class="app-callout__b">TO SEE HOW MUCH NEIGHBORS ARE</div>
    <div class="app-callout__c">ALREADY SAVING!</div>
  </div>

  <div class="abs meter-label" style="left:237px;top:282px">5%</div>
  <div class="abs meter-label" style="left:237px;top:364px">10%</div>

  <div class="abs ribbon-text ribbon-text--lead">Sign up now<br>and receive</div>
  <div class="abs ribbon-text ribbon-text--big">50%<br>OFF</div>
  <div class="abs first-mow">Your First<br>Mow!</div>

  <div class="abs contact back-contact">
    <div><b>CALL US</b> ☏ <span>555-0142-386</span></div>
    <div><b>VISIT US</b> ⊕ <span>www.YardMint.example</span></div>
  </div>

  <div class="abs indicia">PRSRT STD<br>ECRWSS<br>NPDS Postage<br><b>PAID</b><br>RCMX RETAIL</div>

  <div class="abs address">
    <div class="address__route">*****************ECRWSS****</div>
    <div>Local<br>Postal Customer</div>
  </div>
</section>

</body>
</html>
```